Flyer for Pharmacy/Medical Convention

Tri-fold flyer for pharmacy/medical convention. The inside of the flyer we would like to look like a venn diagram, possibly using an image similar to our blue logo

Copy write will be submitted when a design is chosen

there will be a flap about educational features, one about supplements an automated recommendations, and a flap about a computer platform to manage patients

Target Market(s)

Pharmacists and Medical Providers

Industry/Entity Type

Supplement

Colors

Designer to choose colors to be used in the design.

Requirements
Must have
• color scheme similar to logos and or label design attached

```html
<!DOCTYPE html>
<html lang="en">
<head>
<meta charset="utf-8">
<title>Clarion Care Solutions – Convention Flyer</title>
<link href="https://fonts.googleapis.com/css2?family=Open+Sans:wght@400;700;800&display=swap" rel="stylesheet">
<style>
  :root{
    --stage:#1f5a9f;
    --paper:#ffffff;
    --paper-shade:#eef0f3;
    --navy:#1c2f7a;
    --orange:#e96a2b;
    --teal:#1f9c8c;
    --ink:#1d1d1d;
    --photo-light:#dfe4ea;
    --photo-dark:#9aa6b2;
  }
  *{margin:0;padding:0;box-sizing:border-box}
  html,body{width:1200px;height:772px;overflow:hidden}
  body{background:var(--stage);font-family:"Open Sans",Arial,sans-serif;position:relative}

  .page{position:absolute;background:linear-gradient(160deg,var(--paper) 0%,var(--paper-shade) 100%);box-shadow:0 10px 24px rgba(0,0,0,.25);overflow:hidden}
  .page--left{left:40px;top:176px;width:300px;height:420px}
  .page--center{left:370px;top:41px;width:460px;height:690px}
  .page--right{left:860px;top:176px;width:300px;height:420px}

  .brand{position:absolute;display:flex;align-items:center;gap:6px;color:var(--navy);font-weight:700;white-space:nowrap}
  .brand__dot{border-radius:50%;background:var(--navy);flex:none}
  .brand--lg{left:18px;top:18px;font-size:17px}
  .brand--lg .brand__dot{width:16px;height:16px}
  .brand--sm{font-size:10px}
  .brand--sm .brand__dot{width:10px;height:10px}

  .heading{color:var(--orange);font-weight:800;font-size:10px;margin:6px 0 3px}
  .body{font-size:6px;line-height:1.45;color:var(--ink);text-align:justify}
  .col{position:absolute}

  .shape{position:absolute;left:0;top:0}

  .feature{position:absolute;left:22px;top:500px;width:230px}
  .feature .heading{font-size:17px;margin-bottom:5px}
  .feature .body{font-size:9.5px;font-weight:700;line-height:1.4;text-align:left}

  .bubble-label{position:absolute;font-weight:800;font-size:13px;color:var(--ink)}
  .bubble-label span{color:#fff}
</style>
</head>
<body>

<!-- Left panel -->
<section class="page page--left">
  <div class="brand brand--sm" style="left:14px;top:18px"><span class="brand__dot"></span>Clarion Care Solutions</div>
  <div class="col" style="left:14px;top:60px;width:125px">
    <p class="body">Our platform helps pharmacists guide patients with clear education, smart supplement advice and simple tools for daily care.</p>
    <h3 class="heading">Sample Text</h3>
    <p class="body">Our platform helps pharmacists guide patients with clear education, smart supplement advice and simple tools for daily care.</p>
    <h3 class="heading">Sample Text</h3>
    <p class="body">Our platform helps pharmacists guide patients with clear education, smart supplement advice and simple tools for daily care.</p>
  </div>
  <div class="col" style="left:160px;top:18px;width:125px">
    <h3 class="heading">Sample Text</h3>
    <p class="body">Our platform helps pharmacists guide patients with clear education, smart supplement advice and simple tools for daily care.</p>
    <h3 class="heading">Sample Text</h3>
    <p class="body">Our platform helps pharmacists guide patients with clear education, smart supplement advice and simple tools for daily care.</p>
  </div>
</section>

<!-- Center panel -->
<section class="page page--center">
  <svg class="shape" width="460" height="690" viewBox="0 0 460 690">
    <defs>
      <linearGradient id="labPhoto" x1="0" y1="0" x2="1" y2="1">
        <stop offset="0" stop-color="var(--photo-light)"/>
        <stop offset="1" stop-color="var(--photo-dark)"/>
      </linearGradient>
    </defs>
    <rect width="460" height="340" fill="url(#labPhoto)" role="img" aria-label="Photo of a gloved hand handling test tubes in a laboratory"/>
    <polygon points="0,335 95,285 300,285 460,190 460,690 0,690" fill="var(--paper)"/>
    <polyline points="0,335 95,285 300,285 460,190" fill="none" stroke="var(--navy)" stroke-width="4"/>
    <circle cx="300" cy="385" r="82" fill="var(--orange)" opacity=".95"/>
    <circle cx="425" cy="335" r="20" fill="var(--orange)"/>
    <circle cx="390" cy="470" r="72" fill="var(--teal)" opacity=".9"/>
    <circle cx="262" cy="500" r="22" fill="var(--teal)"/>
    <circle cx="360" cy="590" r="58" fill="var(--orange)" opacity=".92"/>
  </svg>
  <div class="brand brand--lg"><span class="brand__dot"></span>Clarion Care Solutions</div>
  <div class="bubble-label" style="left:240px;top:370px">Sample <span>Text</span></div>
  <div class="bubble-label" style="left:345px;top:460px">Sample <span>Text</span></div>
  <div class="bubble-label" style="left:320px;top:582px;font-size:11px">Sample <span>Text</span></div>
  <div class="feature">
    <h2 class="heading">Sample Text</h2>
    <p class="body">Lorem Ipsum is simply dummy text of the printing and typesetting industry. Lorem Ipsum has been the industry's standard dummy text ever since the 1500s, when an unknown printer took a galley of type and scrambled it to make a type specimen book.</p>
  </div>
</section>

<!-- Right panel -->
<section class="page page--right">
  <svg class="shape" width="300" height="420" viewBox="0 0 300 420">
    <defs>
      <linearGradient id="deskPhoto" x1="0" y1="0" x2="1" y2="1">
        <stop offset="0" stop-color="#e8ecf0"/>
        <stop offset="1" stop-color="#8f9aa6"/>
      </linearGradient>
    </defs>
    <rect width="300" height="175" fill="url(#deskPhoto)" role="img" aria-label="Photo of a clinician typing on a laptop at a desk"/>
    <polygon points="0,95 40,80 200,80 300,150 300,420 0,420" fill="var(--paper)"/>
    <polyline points="0,95 40,80 200,80 300,150" fill="none" stroke="var(--navy)" stroke-width="3"/>
  </svg>
  <div class="brand brand--sm" style="left:14px;top:16px"><span class="brand__dot"></span>Clarion Care Solutions</div>
  <div class="col" style="left:14px;top:100px;width:125px">
    <p class="body">Our platform helps pharmacists guide patients with clear education, smart supplement advice and simple tools for daily care.</p>
    <h3 class="heading">Sample Text</h3>
    <p class="body">Our platform helps pharmacists guide patients with clear education, smart supplement advice and simple tools for daily care.</p>
  </div>
  <div class="col" style="left:160px;top:165px;width:125px">
    <h3 class="heading">Sample Text</h3>
    <p class="body">Our platform helps pharmacists guide patients with clear education, smart supplement advice and simple tools for daily care.</p>
    <h3 class="heading">Sample Text</h3>
    <p class="body">Our platform helps pharmacists guide patients with clear education, smart supplement advice and simple tools for daily care.</p>
  </div>
</section>

</body>
</html>
```